Roofing contractor
Maple Ford Creek Roofing needs a postcard
Use content from attached PDF from our last flyer

Target Market(s)

people needing home improvements

Industry/Entity Type

Roofing

Requirements
Must have
• 6x9 inch - is the size of the postcard, double sided (please use the templates attached to the brief itself)
• configured for mail (ZTCM)
• Ok to use stock photography but please try to find royalty-free

```html
<!DOCTYPE html>
<html lang="en">
<head>
<meta charset="utf-8">
<title>Maple Ford Creek Roofing – Postcard</title>
<link rel="stylesheet" href="https://fonts.googleapis.com/css2?family=Roboto+Condensed:ital,wght@0,300;0,400;0,700;1,400&family=Open+Sans:wght@300;400&display=swap">
<style>
:root{
  --coral:#e8735a;
  --blue:#3f73c4;
  --sky:#5d86cf;
  --charcoal:#363636;
  --white:#ffffff;
  --ink:#1e1e1e;
  --rule:#c9c9c9;
  --backdrop:#cfcfcf;
  --photo-a:#6f7f9c;
  --photo-b:#5a6275;
}
*{margin:0;padding:0;box-sizing:border-box}
html,body{width:1200px;height:1200px;overflow:hidden}
body{background:var(--backdrop);font-family:"Roboto Condensed",Arial,sans-serif;position:relative}
.card{position:absolute;left:40px;width:826px;height:559px;overflow:hidden;box-shadow:0 4px 10px rgba(0,0,0,.3)}
.card--front{top:22px;background:var(--coral)}
.card--back{top:616px;background:var(--white)}
.side-label{position:absolute;font-weight:700;font-size:64px;color:var(--ink);letter-spacing:1px}
.side-label--front{left:936px;top:252px}
.side-label--back{left:936px;top:836px}
.abs{position:absolute}

/* front */
.front-sky{left:0;top:0;width:826px;height:116px;background:linear-gradient(180deg,#6a8fd3,var(--sky))}
.brand{font-family:"Open Sans",Arial,sans-serif;font-weight:300;color:var(--white);line-height:1}
.brand--front{left:44px;top:50px}
.brand .name-top{font-size:14px;letter-spacing:.5px}
.brand .name-main{font-size:40px;margin-top:2px}
.contact-top{top:28px;font-size:21px;color:var(--white);display:flex;align-items:center;gap:10px}
.house-photo{left:404px;top:60px;width:422px;height:440px}
.headline{left:46px;top:130px;color:var(--white)}
.headline .kicker{font-weight:300;font-size:33px}
.headline .title{font-weight:700;font-size:40px;margin-top:12px;line-height:1}
.headline .sub{font-weight:700;font-size:28px;margin-top:6px}
.headline .rule{width:322px;height:1px;background:rgba(255,255,255,.6);margin:14px 0 16px}
.headline .story{font-style:italic;font-size:15px;line-height:19px;text-transform:uppercase}
.headline .since{font-weight:700;font-size:22px;text-transform:uppercase;margin-top:2px}
.call-band{left:0;top:360px;width:826px;height:200px}
.call{left:85px;top:370px;color:var(--white)}
.call .num{font-weight:700;font-size:46px;line-height:1}
.call .note{font-family:"Open Sans",Arial,sans-serif;font-weight:300;font-size:21px;line-height:27px;margin-top:2px}
.services{left:0;top:478px;width:826px;height:81px;background:var(--charcoal);display:flex;align-items:center;justify-content:space-around;padding:0 22px 0 30px;color:var(--white);font-size:20px;font-weight:700}
.services li{list-style:none}
.services li::before{content:"";display:inline-block;width:7px;height:7px;border-radius:50%;background:var(--coral);margin-right:8px;vertical-align:middle}

/* back */
.promo-panel{left:0;top:0;width:492px;height:559px;background:var(--coral)}
.promo-title{left:0;width:492px;top:18px;text-align:center;font-size:21px;font-weight:700;color:var(--white);padding-left:30px}
.tile{width:197px;height:94px}
.tile-cap{width:240px;text-align:center;color:var(--white);font-weight:700;font-size:15px}
.offer{left:28px;top:372px;color:var(--white)}
.offer .line1{font-size:25px;font-weight:700;color:var(--white)}
.offer .line1 span{font-weight:400;color:var(--charcoal)}
.offer .line2{font-size:33px;font-weight:700;line-height:1.1}
.back-footer{left:0;top:464px;width:492px;height:95px;background:var(--charcoal);color:var(--white)}
.back-footer .phone{left:58px;top:18px;font-weight:700;font-size:28px}
.back-footer .web{left:58px;top:58px;font-size:17px}
.back-footer .mail{left:282px;top:25px;font-family:"Open Sans",Arial,sans-serif;font-size:14px}
.social-dot{width:16px;height:16px;border-radius:50%;background:var(--white);top:60px}
.brand--back{left:512px;top:44px;color:var(--charcoal)}
.brand--back .name-top{font-size:13px}
.brand--back .name-main{font-size:33px}
.stamp-box{left:726px;top:23px;width:78px;height:78px;border:3px solid var(--charcoal)}
.address-line{left:529px;width:274px;height:1px;background:var(--rule)}
</style>
</head>
<body>

<section class="card card--front" aria-label="Postcard front">
  <div class="abs front-sky"></div>
  <svg class="abs house-photo" viewBox="0 0 422 440" preserveAspectRatio="none" role="img" aria-label="Photo of a two-storey house with a new shingle roof">
    <defs>
      <linearGradient id="photoTone" x1="0" y1="0" x2="1" y2="1">
        <stop offset="0" stop-color="var(--photo-a)"/>
        <stop offset="1" stop-color="var(--photo-b)"/>
      </linearGradient>
    </defs>
    <polygon points="110,0 422,0 422,440 0,440" fill="url(#photoTone)"/>
  </svg>
  <div class="abs brand brand--front">
    <div class="name-top">MAPLE FORD CREEK</div>
    <div class="name-main">ROOFING</div>
  </div>
  <div class="abs contact-top" style="left:277px">
    <svg width="24" height="16" viewBox="0 0 24 16"><rect x="1" y="1" width="22" height="14" fill="none" stroke="#1f2a44" stroke-width="2"/><polyline points="1,1 12,9 23,1" fill="none" stroke="#1f2a44" stroke-width="2"/></svg>
    <span>hello@mfcroofing.com</span>
  </div>
  <div class="abs contact-top" style="left:596px">
    <svg width="18" height="18" viewBox="0 0 18 18"><circle cx="9" cy="9" r="8" fill="none" stroke="#1f2a44" stroke-width="1.5"/><ellipse cx="9" cy="9" rx="3.5" ry="8" fill="none" stroke="#1f2a44" stroke-width="1.5"/><line x1="1" y1="9" x2="17" y2="9" stroke="#1f2a44" stroke-width="1.5"/></svg>
    <span>www.mfcroofing.com</span>
  </div>

  <div class="abs headline">
    <div class="kicker">CONSIDERING A NEW ROOF</div>
    <div class="title">MAPLE FORD CREEK</div>
    <div class="sub">ROOFING &amp; SHEET METAL</div>
    <div class="rule"></div>
    <div class="story">We've been building trust and serving our<br>customers in Maple Ford Creek with</div>
    <div class="since">With integrity since 1995</div>
  </div>

  <svg class="abs call-band" viewBox="0 0 826 200" preserveAspectRatio="none" aria-hidden="true">
    <polygon points="0,22 394,22 390,100 278,118 0,118" fill="var(--blue)"/>
  </svg>
  <svg class="abs" style="left:44px;top:389px" width="22" height="22" viewBox="0 0 22 22" aria-hidden="true"><circle cx="11" cy="11" r="10" fill="none" stroke="#1f2a44" stroke-width="1.5"/><path d="M7 6 l3 0 l1 3 l-2 1 a7 7 0 0 0 3 3 l1 -2 l3 1 l0 3 a9 9 0 0 1 -9 -9z" fill="#1f2a44"/></svg>
  <div class="abs call">
    <div class="num">555-214-7380</div>
    <div class="note">To make an appointment<br>or ask questions</div>
  </div>

  <ul class="abs services">
    <li>Roof Repair</li>
    <li>Skylight Replacement</li>
    <li>Chimney Caps &amp; Repair</li>
    <li>Roof Maintenance</li>
  </ul>
</section>

<section class="card card--back" aria-label="Postcard back">
  <div class="abs promo-panel"></div>
  <div class="abs promo-title">TAKE ADVANTAGE OF OUR 2018 PROMOTIONS</div>

  <div class="abs tile" style="left:28px;top:70px;background:linear-gradient(135deg,#555,#2f2f2f)" role="img" aria-label="Close-up of dark architectural shingles"></div>
  <div class="abs tile-cap" style="left:6px;top:177px">50 YR ARCHITECTURAL SHINGLES</div>
  <div class="abs tile" style="left:261px;top:70px;background:linear-gradient(180deg,#4a7d68,#cfd6d0)" role="img" aria-label="Building with green metal roof"></div>
  <div class="abs tile-cap" style="left:240px;top:177px">PREMIUM METAL ROOFING</div>
  <div class="abs tile" style="left:28px;top:240px;background:linear-gradient(160deg,#a9b8c6,#b8a48c)" role="img" aria-label="Roof edge with gutter and downspout"></div>
  <div class="abs tile-cap" style="left:6px;top:345px">GUTTER &amp; DOWNSPOUT</div>
  <div class="abs tile" style="left:261px;top:240px;background:linear-gradient(160deg,#6b6b6b,#a8a8a8)" role="img" aria-label="Perforated gutter guard on roof edge"></div>
  <div class="abs tile-cap" style="left:240px;top:345px">GUTTER GUARD</div>

  <div class="abs offer">
    <div class="line1">5% to 25% OFF <span>SELECT SERVICES NOW</span></div>
    <div class="line2">THROUGH DECEMBER 31, 2018</div>
  </div>

  <div class="abs back-footer">
    <svg class="abs" style="left:26px;top:26px" width="16" height="16" viewBox="0 0 22 22" aria-hidden="true"><circle cx="11" cy="11" r="10" fill="none" stroke="#fff" stroke-width="1.5"/><path d="M7 6 l3 0 l1 3 l-2 1 a7 7 0 0 0 3 3 l1 -2 l3 1 l0 3 a9 9 0 0 1 -9 -9z" fill="#fff"/></svg>
    <div class="abs phone">555-214-7380</div>
    <svg class="abs" style="left:26px;top:60px" width="16" height="16" viewBox="0 0 18 18" aria-hidden="true"><circle cx="9" cy="9" r="8" fill="none" stroke="#fff" stroke-width="1.5"/><ellipse cx="9" cy="9" rx="3.5" ry="8" fill="none" stroke="#fff" stroke-width="1.5"/><line x1="1" y1="9" x2="17" y2="9" stroke="#fff" stroke-width="1.5"/></svg>
    <div class="abs web">www.mfcroofing.com</div>
    <svg class="abs" style="left:258px;top:29px" width="15" height="11" viewBox="0 0 24 16" aria-hidden="true"><rect x="1" y="1" width="22" height="14" fill="none" stroke="#fff" stroke-width="2"/><polyline points="1,1 12,9 23,1" fill="none" stroke="#fff" stroke-width="2"/></svg>
    <div class="abs mail">hello@mfcroofing.com</div>
    <div class="abs social-dot" style="left:258px"></div>
    <div class="abs social-dot" style="left:294px"></div>
    <div class="abs social-dot" style="left:330px"></div>
  </div>

  <div class="abs brand brand--back">
    <div class="name-top">MAPLE FORD CREEK</div>
    <div class="name-main">ROOFING</div>
  </div>
  <div class="abs stamp-box" aria-label="Postage area"></div>
  <div class="abs address-line" style="top:280px"></div>
  <div class="abs address-line" style="top:318px"></div>
  <div class="abs address-line" style="top:356px"></div>
  <div class="abs address-line" style="top:394px"></div>
</section>

<div class="side-label side-label--front">FRONT</div>
<div class="side-label side-label--back">BACK</div>

</body>
</html>
```